We're a trash valet service. We collect trash that tenants at apartment communitys, elder/assisted liveing would be ideal but we collect Sunday through Thursdays and also offer morning check ups to make sure nothing is left out for pickup. Id like it basic but elegant with little to no cartoon caricatures. But not aposed to them if done right. Colors tequise, orange, blue not married to any of the in spasific.

Lanternway Hauling
Number : 555-314-7290
Address: 438 Quarry Ridge Road SUITE
Millbrook NJ 08000
Email: Marla@lanternway-hauling.example

I attached my logo.
Those don't have to be the colors plain black is fine for the broshour but I do like those colors with orange maybe.
Updates

Everyone is doing such amazing work. I wanted to just make sure I let everyone know what I need and what should not be on broshour. We do not have garbage trucks, we just both of trash in on site dumpsters or compactors. We use tall kitchen cans for residents to put their garbage in and on in the cans outside of their doors. Pictures of hallways with cans with our logo on it would be good definitely no one's face. What we provide for managers and their benefiting from our service. residents expierance. We also don't have a QR code scanner. And the morning check up is an added service.

Target Market(s)

Apartment communitys

Requirements
Should not have
• Garbage trucks

```html
<!DOCTYPE html>
<html lang="en">
<head>
<meta charset="utf-8">
<title>Lanternway Hauling – Trifold Brochure</title>
<link href="https://fonts.googleapis.com/css2?family=Montserrat:wght@400;500;600;700;800&family=Great+Vibes&display=swap" rel="stylesheet">
<style>
:root{
  --navy:#16284d;
  --orange:#ef7a23;
  --teal:#1a93a8;
  --panel-gray:#ececec;
  --ink:#222831;
  --white:#ffffff;
  --black:#111111;
  --backdrop:#9a9a9a;
}
*{margin:0;padding:0;box-sizing:border-box}
html,body{width:1200px;height:2698px;overflow:hidden}
body{background:var(--backdrop);font-family:"Montserrat",sans-serif;color:var(--ink);position:relative}
.spread{position:absolute;left:54px;width:780px;height:636px;transform:scale(1.4);transform-origin:0 0;overflow:hidden;background:var(--white);box-shadow:0 4px 18px rgba(0,0,0,.25)}
.spread-outside{top:419px}
.spread-inside{top:1389px}
.abs{position:absolute}
.shapes{position:absolute;left:0;top:0;width:780px;height:636px}
.photo{position:absolute}

/* brand lockup */
.brand{position:absolute;display:flex;align-items:center;gap:7px}
.brand-mark{width:26px;height:26px;border:3px solid currentColor}
.brand-name{font-weight:800;font-size:13px;line-height:1.05;text-transform:uppercase;letter-spacing:.2px}

/* outside */
.cover-back{left:0;top:0;width:255px;height:636px}
.headline{position:absolute;left:30px;top:30px;font-weight:800;font-size:23px;line-height:1;color:var(--navy)}
.headline span{display:block;color:var(--orange)}
.intro{position:absolute;left:30px;top:98px;width:200px;font-size:9px;line-height:1.6}
.script{font-family:"Great Vibes",cursive;font-weight:400}
.tagline{position:absolute;left:26px;top:545px;color:var(--white)}
.tagline .script{font-size:26px;line-height:1}
.tagline strong{display:block;font-size:15px;font-weight:700}

.contact-panel{position:absolute;left:255px;top:0;width:257px;height:636px;background:var(--panel-gray)}
.dash{position:absolute;left:50%;transform:translateX(-50%);top:184px;width:34px;height:2px;background:linear-gradient(90deg,var(--orange) 50%,var(--navy) 50%)}
.contact-title{position:absolute;top:198px;width:100%;text-align:center;font-weight:600;font-size:12.5px;letter-spacing:1.6px}
.contact-item{position:absolute;width:100%;text-align:center;font-size:10px;line-height:1.35}
.contact-item .icon{display:block;margin:0 auto 8px;width:44px;height:44px;border-radius:50%;background:var(--navy)}
.site-line{position:absolute;width:100%;text-align:center;font-size:10px;letter-spacing:1.6px}
.site-line::before,.site-line::after{content:"";display:inline-block;width:24px;height:1px;background:currentColor;vertical-align:middle;margin:0 5px}

.cover{position:absolute;left:512px;top:0;width:268px;height:636px;text-align:center;color:var(--white)}
.cover-text{position:absolute;top:442px;width:100%}
.cover-text .kicker{font-weight:700;font-size:20px;line-height:1}
.cover-text .big{font-weight:800;font-size:33px;line-height:1.05}
.cover-text .script{font-size:27px;line-height:1.1;margin-top:2px}
.cover-text .sub{font-weight:700;font-size:15px}

/* inside */
.pill{position:absolute;height:24px;border-radius:12px;color:var(--white);font-weight:600;font-size:14px;text-align:center;line-height:24px;letter-spacing:.3px}
.pill-navy{background:var(--navy)}
.pill-orange{background:var(--orange)}
.service{position:absolute;left:30px;width:220px;display:flex;gap:10px}
.service .icon{flex:none;width:40px;height:40px;border-radius:50%}
.icon-teal{background:var(--teal)}
.icon-navy{background:var(--navy)}
.service h3,.step h3{font-size:9.5px;font-weight:700;line-height:1.3}
.service p,.step p{font-size:8.3px;line-height:1.25}
.step{position:absolute;left:292px;width:190px;display:flex;gap:12px}
.step .num{flex:none;width:26px;height:26px;border-radius:50%;background:var(--teal);color:var(--white);font-size:12px;font-weight:600;text-align:center;line-height:26px}
.step-rail{position:absolute;left:305px;top:176px;height:128px;border-left:1.5px dotted var(--teal)}
.inside-contact{position:absolute;left:36px;top:588px;color:var(--white);font-size:11px;line-height:1.25}
.inside-contact .web{letter-spacing:1.4px}
.review{position:absolute;left:540px;width:225px;height:72px;border:1px solid #b8bcc4;border-radius:8px;padding:18px 12px 0}
.review .quotes{position:absolute;left:12px;top:-10px;display:flex;gap:3px}
.review .quotes i{display:block;width:20px;height:20px;border-radius:50%}
.review p{font-size:7.6px;line-height:1.35}
.review cite{display:block;font-style:italic;font-weight:700;font-size:7.6px;margin-top:3px}
svg.ic{display:block}
</style>
</head>
<body>

<!-- OUTSIDE -->
<section class="spread spread-outside" aria-label="Brochure outside">
  <div class="photo" role="img" aria-label="Smiling attendant carrying a bagged trash bag to a wheeled bin, no face shown in final art" style="left:0;top:150px;width:255px;height:340px;background:linear-gradient(160deg,#d9d2c0 0%,#9b6b4e 40%,#5a3a2e 70%,#2f5a3c 100%)"></div>
  <div class="photo" role="img" aria-label="Staff placing bagged trash into an on-site dumpster at an apartment community" style="left:512px;top:60px;width:268px;height:330px;background:linear-gradient(170deg,#c9d6df 0%,#b7b8b3 35%,#8d9a7a 65%,#e3e3df 100%)"></div>

  <svg class="shapes" viewBox="0 0 780 636" aria-hidden="true">
    <path d="M0 452 C90 410 175 470 255 492 L255 506 C175 484 90 424 0 466Z" fill="var(--orange)"/>
    <path d="M0 462 C90 420 175 482 255 504 L255 522 C175 500 90 440 0 480Z" fill="var(--teal)"/>
    <path d="M0 476 C90 436 175 498 255 518 L255 636 L0 636Z" fill="var(--navy)"/>
    <path d="M480 0 H780 V118 C700 140 575 120 530 50 C515 25 500 10 480 0Z" fill="var(--black)"/>
    <path d="M512 405 C590 360 690 350 780 335 V350 C690 365 590 378 512 420Z" fill="var(--teal)"/>
    <path d="M512 415 C590 372 690 362 780 346 V636 H512Z" fill="var(--orange)"/>
  </svg>

  <div class="cover-back">
    <h1 class="headline">TRASH VALET<span>DONE RIGHT</span></h1>
    <p class="intro">We provide dependable, discreet trash collection and area checks to keep your community clean, safe, and compliant.</p>
    <p class="tagline"><span class="script">Cleaner Grounds</span><strong>HAPPIER RESIDENTS</strong></p>
  </div>

  <div class="contact-panel" style="background:none">
    <div class="brand" style="left:48px;top:26px;color:var(--black)"><span class="brand-mark"></span><span class="brand-name">Lanternway<br>Hauling LLC</span></div>
    <div class="dash"></div>
    <p class="contact-title">CONTACT US TODAY!</p>
    <p class="contact-item" style="top:230px"><span class="icon"><svg class="ic" viewBox="0 0 44 44" width="44" height="44"><path d="M16 13c1-1 2.5-1 3 0l2 4c.5 1 0 2-1 2.5l-1 .8c1 2.5 3 4.5 5.5 5.7l.8-1c.6-1 1.6-1.3 2.5-.8l4 2c1 .5 1 2 0 3l-2 2c-6 .5-15-8.5-15-15z" fill="none" stroke="#fff" stroke-width="1.6"/></svg></span>555-314-7290</p>
    <p class="contact-item" style="top:320px"><span class="icon"><svg class="ic" viewBox="0 0 44 44" width="44" height="44"><path d="M22 33s-8-8-8-14a8 8 0 0 1 16 0c0 6-8 14-8 14z" fill="none" stroke="#fff" stroke-width="1.6"/><circle cx="22" cy="19" r="3" fill="none" stroke="#fff" stroke-width="1.6"/></svg></span>438 Quarry Ridge Road SUITE<br>Millbrook NJ 08000</p>
    <p class="contact-item" style="top:420px"><span class="icon"><svg class="ic" viewBox="0 0 44 44" width="44" height="44"><rect x="12" y="15" width="20" height="14" fill="none" stroke="#fff" stroke-width="1.6"/><path d="M12 15l10 8 10-8" fill="none" stroke="#fff" stroke-width="1.6"/></svg></span>Marla@lanternway-hauling.example</p>
    <p class="site-line" style="top:580px">lanternway-hauling.example</p>
  </div>

  <div class="cover">
    <div class="brand" style="left:48px;top:30px;color:var(--white)"><span class="brand-mark"></span><span class="brand-name">Lanternway<br>Hauling LLC</span></div>
    <div class="cover-text">
      <div class="kicker">TRASH VALET</div>
      <div class="big">MADE EASY</div>
      <div class="script">Reliable Services</div>
      <div class="sub">CLEANER COMMUNITIES</div>
    </div>
    <p class="site-line" style="top:580px;color:var(--white)">lanternway-hauling.example</p>
  </div>
</section>
<style>.spread-outside{background:linear-gradient(90deg,var(--white) 0 255px,var(--panel-gray) 255px 512px,var(--white) 512px)}</style>

<!-- INSIDE -->
<section class="spread spread-inside" aria-label="Brochure inside">
  <div class="photo" role="img" aria-label="Row of suburban apartment townhomes with green lawns and trees" style="left:0;top:395px;width:440px;height:241px;background:linear-gradient(180deg,rgba(255,255,255,0) 0%,#b9cfe0 10%,#6f8a5e 45%,#8a8270 70%,#c9c6bd 100%);-webkit-mask-image:linear-gradient(90deg,#000 70%,transparent);mask-image:linear-gradient(90deg,#000 70%,transparent)"></div>
  <div class="photo" role="img" aria-label="Worker carrying a black trash bag past wheeled bins, no face shown" style="left:430px;top:0;width:350px;height:215px;background:linear-gradient(135deg,#8a9b84 0%,#4d5a58 45%,#1e1e22 70%,#7b7d80 100%)"></div>

  <svg class="shapes" viewBox="0 0 780 636" aria-hidden="true">
    <path d="M430 0 C450 130 570 200 780 188 V230 H430Z" fill="var(--white)"/>
    <path d="M430 0 C450 130 570 200 780 188" fill="none" stroke="var(--teal)" stroke-width="6"/>
    <path d="M440 0 C462 120 575 188 780 178" fill="none" stroke="var(--navy)" stroke-width="2"/>
    <path d="M0 520 C60 530 140 590 250 636 H0Z" fill="var(--navy)"/>
    <path d="M0 506 C70 516 150 576 275 636 H258 C150 590 70 532 0 522Z" fill="var(--teal)"/>
  </svg>

  <div class="brand" style="left:36px;top:26px;color:var(--black)"><span class="brand-mark"></span><span class="brand-name">Lanternway<br>Hauling LLC</span></div>

  <div class="pill pill-navy" style="left:30px;top:100px;width:200px">OUR SERVICES</div>
  <div class="service" style="top:140px"><span class="icon icon-teal"><svg class="ic" viewBox="0 0 40 40" width="40" height="40"><path d="M13 14h14M17 14v-2h6v2M15 14l1 14h8l1-14M18.5 17v8M21.5 17v8" fill="none" stroke="#fff" stroke-width="1.5"/></svg></span><div><h3>TRASH COLLECTION</h3><p>We collect trash from designated areas Sunday through Thursday evenings.</p></div></div>
  <div class="service" style="top:202px"><span class="icon icon-navy"><svg class="ic" viewBox="0 0 40 40" width="40" height="40"><circle cx="18" cy="18" r="6" fill="none" stroke="#fff" stroke-width="1.6"/><path d="M22.5 22.5l6 6" stroke="#fff" stroke-width="2"/></svg></span><div><h3>MORNING CHECK UPS</h3><p>We return each morning to ensure no trash is left out and your property looks its best</p></div></div>
  <div class="service" style="top:264px"><span class="icon icon-teal"><svg class="ic" viewBox="0 0 40 40" width="40" height="40"><path d="M20 11l8 3v6c0 5-4 8-8 9-4-1-8-4-8-9v-6z" fill="none" stroke="#fff" stroke-width="1.5"/><path d="M16 20l3 3 5-6" fill="none" stroke="#fff" stroke-width="1.6"/></svg></span><div><h3>RELIABLE</h3><p>Our team is punctual, professional and committed to keeping your community clean</p></div></div>
  <div class="service" style="top:326px"><span class="icon icon-navy"><svg class="ic" viewBox="0 0 40 40" width="40" height="40"><rect x="14" y="12" width="12" height="17" fill="none" stroke="#fff" stroke-width="1.5"/><path d="M17 16h2M21 16h2M17 20h2M21 20h2M17 24h2M21 24h2" stroke="#fff" stroke-width="1.4"/></svg></span><div><h3>IDEAL FOR</h3><p>Apartment communities elderly &amp; assited living facilities and property managers.</p></div></div>

  <div class="inside-contact"><div>555-314-7290</div><div class="web">lanternway-hauling.example</div></div>

  <div class="pill pill-orange" style="left:285px;top:98px;width:200px">HOW IT WORKS</div>
  <div class="step-rail"></div>
  <div class="step" style="top:150px"><span class="num">01</span><div><h3>WE COLLECT</h3><p>Our team collects trash from designated areas Sunday through Thursday evening</p></div></div>
  <div class="step" style="top:222px"><span class="num">02</span><div><h3>WE CHECK</h3><p>Each morning, we perform area check ups to ensure no trash is left out.</p></div></div>
  <div class="step" style="top:290px"><span class="num">03</span><div><h3>WE KEEP IT CLEAN</h3><p>We keep your community clean, safe, and compliant</p></div></div>

  <div class="pill pill-navy" style="left:550px;top:252px;width:210px">CLIENT REVIEWS</div>
  <div class="review" style="top:300px"><span class="quotes"><i style="background:var(--navy)"></i><i style="background:var(--orange)"></i></span><p>Lorem Ipsum is simply dummy text of the printing and typesetting industry. Lorem Ipsum has been the industry's standard dummy text ever since</p><cite>- Tomas Reyl</cite></div>
  <div class="review" style="top:402px"><span class="quotes"><i style="background:var(--navy)"></i><i style="background:var(--orange)"></i></span><p>Lorem Ipsum is simply dummy text of the printing and typesetting industry. Lorem Ipsum has been the industry's standard dummy text ever since</p><cite>- Tomas Reyl</cite></div>
  <div class="review" style="top:504px"><span class="quotes"><i style="background:var(--navy)"></i><i style="background:var(--orange)"></i></span><p>Lorem Ipsum is simply dummy text of the printing and typesetting industry. Lorem Ipsum has been the industry's standard dummy text ever since</p><cite>- Tomas Reyl</cite></div>
</section>

</body>
</html>
```